New Business Card Design Project

hello again,
i have an awful year and we were not able to complete our logo plan. we would like to use our #1 logo for business card design process. the primary colors for business card should be white background with orange & black letters. our business is mobil truck cranes. we deliver heavy stuff and unload cargo with crane that is mounted on our trucks.
here is our business card info:
HARBOR LIFT HAULERS, INC.
428 WESTCOTT AVE
MERRICK, NY 11542
OFFICE - 516 487 3091
DIRECT - 1 888 LIFT HAULS
MARK@HLHAULERS.COM
PLEASE also try to get our slogan on card .... "Our Loads Keep Rollin"
lastly please also put "24 hour Knuckleboom Service"
you can call me anytime 24/7 to discuss...my cell # is: 516 759 2036
please also list: Mark Delroy, President
Target Market(s)
Heavy Construction industry
Industry/Entity Type
heavy construction industry
Contact Information for Business Card
24 Hr Knuckleboom Service

```html
<!DOCTYPE html>
<html lang="en">
<head>
<meta charset="utf-8">
<title>Harbor Lift Haulers — Business Card</title>
<link rel="stylesheet" href="https://fonts.googleapis.com/css2?family=Montserrat:wght@300;400;600;800&display=swap">
<style>
  :root {
    --bg: #e6e6e4;
    --paper: #fbfbfa;
    --orange: #e8792a;
    --black: #161616;
    --white: #ffffff;
  }
  * { box-sizing: border-box; margin: 0; padding: 0; }
  html, body { width: 1200px; height: 801px; overflow: hidden; }
  body {
    background: var(--bg);
    font-family: "Montserrat", sans-serif;
    display: flex;
    align-items: center;
    justify-content: center;
    gap: 40px;
  }
  .card {
    position: relative;
    width: 560px;
    height: 320px;
    background: var(--paper);
    overflow: hidden;
    box-shadow: 0 6px 18px rgba(0,0,0,.12);
  }

  /* ---------- Front ---------- */
  .front .band {
    position: absolute;
    left: 190px; right: 0; bottom: 0;
    height: 150px;
    background: var(--orange);
    border-top-left-radius: 40px;
  }
  .front .rule {
    position: absolute;
    left: 290px; right: 0; top: 160px;
    height: 5px;
    background: var(--black);
  }
  .front .truck {
    position: absolute;
    left: 186px; top: 26px;
    width: 112px; height: 274px;
    background: linear-gradient(160deg, #2a2a2a 0%, #161616 70%, #c9661f 100%);
    border-radius: 6px;
  }
  .front .person {
    position: absolute;
    left: 22px; top: 140px;
    width: 156px;
  }
  .person .name {
    color: var(--orange);
    font-weight: 800;
    font-size: 19px;
    letter-spacing: .3px;
    text-transform: uppercase;
    white-space: nowrap;
  }
  .person .title {
    color: var(--black);
    font-weight: 400;
    font-size: 14px;
    margin-top: 2px;
  }
  .front .brand {
    position: absolute;
    left: 310px; top: 34px;
    width: 235px;
    text-align: center;
  }
  .brand .slogan {
    color: var(--orange);
    font-weight: 800;
    font-size: 13px;
    text-transform: uppercase;
    letter-spacing: .5px;
  }
  .brand .company {
    margin-top: 8px;
    color: var(--black);
    font-weight: 800;
    font-size: 24px;
    line-height: 1.05;
    text-transform: uppercase;
  }
  .front .contact {
    position: absolute;
    left: 318px; top: 180px;
    list-style: none;
    color: var(--white);
    font-size: 12px;
    font-weight: 400;
    letter-spacing: .4px;
  }
  .contact li { display: flex; align-items: center; gap: 8px; height: 21px; white-space: nowrap; }
  .contact svg { width: 14px; height: 14px; flex: none; }
  .front .address {
    position: absolute;
    left: 340px; top: 252px;
    color: var(--white);
    font-style: normal;
    font-size: 12px;
    letter-spacing: .4px;
    line-height: 1.45;
    white-space: nowrap;
  }

  /* ---------- Back ---------- */
  .back .brand {
    position: absolute;
    left: 0; right: 0; top: 70px;
    text-align: center;
  }
  .back .brand .slogan { font-size: 16px; }
  .back .brand .company { font-size: 32px; }
  .back .service-band {
    position: absolute;
    left: 0; right: 0; bottom: 36px;
    height: 46px;
    background: var(--orange);
    display: flex;
    align-items: center;
    justify-content: center;
    color: var(--black);
    font-weight: 600;
    font-size: 15px;
    letter-spacing: .6px;
    text-transform: uppercase;
  }
  .back .base-stripe {
    position: absolute;
    left: 0; right: 0; bottom: 12px;
    height: 16px;
    background: var(--orange);
  }
</style>
</head>
<body>

  <section class="card front">
    <div class="band"></div>
    <div class="rule"></div>
    <div class="truck" role="img" aria-label="Black silhouette of a knuckleboom crane truck with orange wheels and raised boom"></div>

    <div class="person">
      <p class="name">Mark Delroy</p>
      <p class="title">President</p>
    </div>

    <div class="brand">
      <p class="slogan">Our Loads Keep Rollin</p>
      <p class="company">Harbor Lift Haulers, Inc.</p>
    </div>

    <ul class="contact">
      <li>
        <svg viewBox="0 0 14 14"><circle cx="7" cy="7" r="7" fill="#161616"/><path d="M4.5 3.8l1.4-.3.7 1.7-.8.6a5 5 0 0 0 2.4 2.4l.6-.8 1.7.7-.3 1.4c-3.3.2-6-2.5-5.7-5.7z" fill="#e8792a"/></svg>
        516 487 3091
      </li>
      <li>
        <svg viewBox="0 0 14 14"><circle cx="7" cy="7" r="7" fill="#161616"/><rect x="3.5" y="4.5" width="7" height="5" fill="none" stroke="#e8792a" stroke-width="1"/><path d="M3.5 4.5L7 7.3l3.5-2.8" fill="none" stroke="#e8792a" stroke-width="1"/></svg>
        1 888 LIFT HAULS
      </li>
      <li>
        <svg viewBox="0 0 14 14"><circle cx="7" cy="7" r="7" fill="#161616"/><circle cx="7" cy="7" r="3.5" fill="none" stroke="#e8792a" stroke-width="1"/><path d="M3.5 7h7M7 3.5c-1.5 2-1.5 5 0 7M7 3.5c1.5 2 1.5 5 0 7" fill="none" stroke="#e8792a" stroke-width=".8"/></svg>
        MARK@HLHAULERS.COM
      </li>
    </ul>

    <address class="address">
      428 WESTCOTT AVE<br>
      MERRICK<br>
      NY 11542
    </address>
  </section>

  <section class="card back">
    <div class="brand">
      <p class="slogan">Our Loads Keep Rollin</p>
      <p class="company">Harbor Lift Haulers, Inc.</p>
    </div>
    <div class="service-band">24 Hour Knuckleboom Service</div>
    <div class="base-stripe"></div>
  </section>

</body>
</html>
```